Wills & Estates legal firm needing A4 presentation folder design

We need a more corporate but family orientated looking presentation folder incorporating existing logo. Needs to be clean lines but warm not clinical. Will contain all documents a family needs when someone dies. Not looking for traditional legal symbols of scales etc. Potential that the design can flow through to letterhead, document front covers, brochures, business cards etc for a complete corporate identity. We are only a firm of one fee earner and cater to a mum and dad market

Industry/Entity Type

Law Firm

Font styles to use
Other font styles liked:
• Univers LT std 57 cn

Colors
ec1f27
848484

Requirements
Must have
• Existing logo
• Area for contact details on back of folder
• Incorporating existing red an grey colours
Should not have
• legal symbols

```html
<!DOCTYPE html>
<html lang="en">
<head>
<meta charset="utf-8">
<title>Kinfield Legal – Presentation Folder</title>
<link href="https://fonts.googleapis.com/css2?family=Didact+Gothic&display=swap" rel="stylesheet">
<style>
  :root {
    --brand-red: #c3122f;
    --brand-red-deep: #a90f29;
    --slate: #4a5560;
    --paper: #ffffff;
    --backdrop-light: #f2f2f2;
    --backdrop-dark: #c9c9c9;
    --rule-light: #e9ecef;
  }
  html, body {
    margin: 0;
    padding: 0;
    width: 1200px;
    height: 958px;
    overflow: hidden;
  }
  body {
    background: radial-gradient(ellipse at 60% 20%, var(--backdrop-light), var(--backdrop-dark));
    font-family: "Didact Gothic", "Century Gothic", sans-serif;
  }
  .folder-spread {
    display: block;
    width: 1200px;
    height: 958px;
  }
  .panel-paper { fill: var(--paper); }
  .pocket { fill: url(#pocketShade); }
  .divider-stripe { fill: none; stroke: var(--slate); stroke-width: 7; stroke-linejoin: miter; }
  .divider-hairline { fill: none; stroke: var(--rule-light); stroke-width: 1; }
  .spine-fold { stroke: rgba(0,0,0,0.08); stroke-width: 1; }
  .wordmark-front { fill: var(--brand-red); font-size: 27px; font-family: "Didact Gothic", sans-serif; }
  .wordmark-back { fill: var(--paper); font-size: 19px; font-family: "Didact Gothic", sans-serif; }
  .contact-line { fill: var(--paper); font-size: 7.5px; font-family: "Didact Gothic", sans-serif; letter-spacing: 0.2px; }
  .web-address { fill: var(--paper); font-size: 9.5px; font-family: "Didact Gothic", sans-serif; letter-spacing: 0.4px; }
</style>
</head>
<body>
<svg class="folder-spread" viewBox="0 0 1200 958" xmlns="http://www.w3.org/2000/svg" aria-label="Kinfield Legal presentation folder, back and front covers">
  <defs>
    <linearGradient id="pocketShade" x1="0" x2="1" y1="0" y2="0">
      <stop offset="0" stop-color="var(--brand-red-deep)"/>
      <stop offset="0.3" stop-color="var(--brand-red)"/>
      <stop offset="0.5" stop-color="var(--brand-red-deep)"/>
      <stop offset="0.7" stop-color="var(--brand-red)"/>
      <stop offset="1" stop-color="var(--brand-red-deep)"/>
    </linearGradient>
  </defs>

  <!-- Paper: back cover (left) and front cover (right) -->
  <g class="folder">
    <rect class="panel-paper" x="200" y="196" width="800" height="566"/>

    <!-- Red lower pocket with raised tab across the spine -->
    <path class="pocket" d="M200 388 H520 L528 378 H672 L680 388 H1000 V762 H200 Z"/>

    <!-- Slate divider stripe tracing the pocket edge -->
    <path class="divider-stripe" d="M200 384.5 H518.5 L526.5 374.5 H673.5 L681.5 384.5 H1000"/>
    <path class="divider-hairline" d="M200 388.5 H520 L528 378.5 H672 L680 388.5 H1000"/>

    <line class="spine-fold" x1="600" y1="196" x2="600" y2="762"/>
  </g>

  <!-- Front cover -->
  <g class="front-cover">
    <text class="wordmark-front" x="945" y="296" text-anchor="end">Kinfield Legal</text>
    <text class="web-address" x="960" y="712" text-anchor="end">www.kinfieldlegal.com.au</text>
  </g>

  <!-- Back cover: contact details -->
  <g class="back-cover">
    <text class="wordmark-back" x="240" y="690">Kinfield Legal</text>
    <text class="contact-line" x="240" y="705">14 Elm Road, NORTHBANK VIC 3000 · T: 03 5550 1482</text>
    <text class="contact-line" x="240" y="716">E: office@kinfieldlegal.com.au · www.kinfieldlegal.com.au</text>
  </g>
</svg>
</body>
</html>
```